KVR Biz Cards

We are a property management company that manages luxury level residential estates. As such, we need a business card design that gives a high end feel. The idea at the moment is to list the services offered on the back of the card, and our company information on the front of the card.

Services for the back of the card are as follows:
Professional Property Management service, Home Hosting & Concierge Service, Holliday Home / Income Property Management

```html
<!DOCTYPE html>
<html lang="en">
<head>
<meta charset="utf-8">
<title>KVR Business Cards</title>
<link href="https://fonts.googleapis.com/css2?family=Montserrat:wght@400;500;600;700&display=swap" rel="stylesheet">
<style>
  :root {
    --bg: #3a3a3a;
    --card: #1d1d1e;
    --card-hi: #2a2a2b;
    --gold: #e8b923;
    --gold-deep: #c99a12;
    --white: #f4f4f4;
    --rule: #8a8a8a;
  }
  * { margin: 0; padding: 0; box-sizing: border-box; }
  html, body { width: 1200px; height: 1200px; overflow: hidden; }
  body {
    background: var(--bg);
    font-family: "Montserrat", sans-serif;
    display: flex; flex-direction: column; align-items: center; justify-content: center; gap: 60px;
  }
  .card {
    position: relative;
    width: 900px; height: 514px;
    border-radius: 34px;
    background: linear-gradient(135deg, var(--card-hi), var(--card) 55%);
    overflow: hidden;
    color: var(--white);
  }
  .brand { display: flex; align-items: center; gap: 14px; color: var(--gold); font-weight: 600; letter-spacing: 6px; }
  .brand-square { width: 26px; height: 26px; background: var(--gold); }

  /* back */
  .card-back { display: flex; flex-direction: column; align-items: center; padding-top: 90px; }
  .card-back .brand { font-size: 84px; }
  .services-title { margin-top: 36px; color: var(--gold); font-weight: 600; font-size: 24px; letter-spacing: 1px; }
  .services-list { list-style: none; margin-top: 14px; text-align: center; font-size: 25px; line-height: 1.5; font-weight: 500; }
  .services-list li::before { content: "• "; }
  .gold-edge { position: absolute; left: 0; right: 0; bottom: 0; height: 14px; background: linear-gradient(90deg, var(--gold-deep), var(--gold), var(--gold-deep)); }

  /* front */
  .card-front .brand { position: absolute; top: 60px; left: 50%; transform: translateX(-50%); font-size: 80px; }
  .company { position: absolute; top: 200px; left: 0; right: 0; text-align: center; }
  .company-name { font-size: 38px; font-weight: 700; letter-spacing: 2px; }
  .company-tagline { color: var(--gold); font-size: 22px; font-weight: 500; margin-top: 4px; letter-spacing: 1px; }
  .divider { position: absolute; left: 450px; top: 330px; width: 1px; height: 130px; background: var(--rule); }
  .person { position: absolute; left: 80px; top: 360px; padding-left: 24px; border-left: 6px solid var(--gold); }
  .person-name { color: var(--gold); font-size: 40px; font-weight: 600; line-height: 1.1; }
  .person-role { font-size: 22px; font-weight: 500; margin-top: 4px; }
  .contacts { position: absolute; left: 500px; top: 335px; list-style: none; font-size: 21px; }
  .contacts li { display: flex; align-items: center; gap: 14px; height: 32px; }
  .contacts svg { width: 20px; height: 20px; fill: none; stroke: var(--gold); stroke-width: 2; }
</style>
</head>
<body>
  <section class="card card-back">
    <div class="brand"><span class="brand-square"></span>KVR</div>
    <h2 class="services-title">SERVICES:</h2>
    <ul class="services-list">
      <li>Professional Property Management service</li>
      <li>Home Hosting &amp; Concierge Service</li>
      <li>Holliday Home / Income Property Management</li>
    </ul>
    <div class="gold-edge"></div>
  </section>

  <section class="card card-front">
    <div class="brand"><span class="brand-square"></span>KVR</div>
    <div class="company">
      <h1 class="company-name">KAVRELL MANAGEMENT</h1>
      <p class="company-tagline">Crafted to Keep Every Home at Ease</p>
    </div>
    <div class="divider"></div>
    <div class="person">
      <p class="person-name">ELLIOT MARSH</p>
      <p class="person-role">CEO | FOUNDER</p>
    </div>
    <ul class="contacts">
      <li><svg viewBox="0 0 20 20"><rect x="5" y="1.5" width="10" height="17" rx="2"/></svg>+000 000 0000</li>
      <li><svg viewBox="0 0 20 20"><path d="M4 2l4 1 1 4-2 2a11 11 0 0 0 5 5l2-2 4 1 1 4c-9 1-16-6-15-15z"/></svg>+000 000 0000</li>
      <li><svg viewBox="0 0 20 20"><circle cx="10" cy="10" r="8"/><path d="M2 10h16M10 2c-4 5-4 11 0 16M10 2c4 5 4 11 0 16"/></svg>www.example.com</li>
      <li><svg viewBox="0 0 20 20"><rect x="2" y="4" width="16" height="12"/><path d="M2 4l8 7 8-7"/></svg>contact@example.com</li>
    </ul>
  </section>
</body>
</html>
```